Restwell Path App - Featured Graphics/Screenshots and Icon

We need graphics for a new app that is a step-by-step program for treating insomnia.
What is needed:
1) app icon (1024x1024 so it can be scaled down)
2) general featured image for use in advertising and app stores
3) screenshots incorporating text (Based on Cognitive Behavioral Therapy for Insomnia, An Innovative and Interactive Self-Help Program, Recommendations Tailored to Your Sleep Patterns, Track Your Sleep).
We have included a variety of example screenshots from the app.
Example text to include with screenshots and/or feature graphics.
1. Based on Cognitive Behavioral Therapy for Insomnia (CBT-I)
2. CBT-I is recommended as a wise choice by buyer digest and a first-line treatment approach by the Federal Bureau of Wellness (FBW)
3. An Innovative and Interactive Self-Help Program
4. Recommendations Tailored to Your Sleep Patterns
5. Track Your Sleep
Here is an overview of the program:
The Restwell Path is an app developed to enable more access to cognitive-behavior therapy for insomnia (CBT-I). CBT-I is recognized as a first line treatment approach by the Federal Bureau of Wellness, however there are few trained providers of the treatment. The Restwell Path will guide you through the cognitive-behavioral treatment process in a step-by-step manner. You will be introduced to new steps on a weekly basis. The first step is to establish a baseline using sleep logs. This is very important as the information gathered will be used to set your initial sleep/wake schedule. Following this initial step, you will be guided through a process of re-establishing a natural drive to sleep, resetting your circadian rhythm, learning to recognize/manage anxiety, apply productive ways to think about sleep, and ways to prevent relapse. The treatment approach can be challenging. It will require completion of all tasks and maintaining the recommended sleep schedule.
We prefer layered PSD files to allow for easy scaling and / or alteration.
Target Market(s)
Mobile app users with insomnia.
Look and feel

```html
<!DOCTYPE html>
<html lang="en">
<head>
<meta charset="utf-8">
<title>Restwell Path App – Sleep Chart</title>
<link rel="stylesheet" href="https://fonts.googleapis.com/css2?family=Roboto:wght@400;500;700&display=swap">
<style>
  :root {
    --status-black: #050505;
    --nav-blue-top: #2a6fc0;
    --nav-blue-bottom: #164f98;
    --toolbar-blue: #1d4a86;
    --control-blue: #2a63ae;
    --control-border: #5a8fd2;
    --panel-navy: #2b3447;
    --panel-navy-deep: #232b3b;
    --chart-fill: #3f7fc6;
    --chart-line: #8fbbea;
    --axis-line: rgba(255,255,255,0.55);
    --tag-green: #8fbf3a;
    --text-white: #ffffff;
    --text-soft: #b9c6da;
    --refresh-grey: #c9d3e2;
    --photo-light: #f3ece8;
    --photo-pink: #e9b3c4;
    --photo-warm: #e8cfae;
  }
  * { box-sizing: border-box; margin: 0; padding: 0; }
  html, body { width: 1200px; height: 2352px; overflow: hidden; }
  body { font-family: "Roboto", Arial, sans-serif; color: var(--text-white); background: var(--panel-navy-deep); }

  .app-screen { position: relative; width: 1200px; height: 2352px; display: flex; flex-direction: column; }

  .status-bar {
    height: 78px; background: var(--status-black);
    display: flex; align-items: center; justify-content: space-between;
    padding: 0 28px; font-size: 34px; font-weight: 500; flex-shrink: 0;
  }
  .status-left, .status-right { display: flex; align-items: center; gap: 14px; width: 320px; }
  .status-right { justify-content: flex-end; }
  .signal-dots { display: flex; gap: 6px; }
  .signal-dots i { width: 16px; height: 16px; border-radius: 50%; background: var(--text-white); display: block; }
  .signal-dots i.off { background: none; border: 2px solid var(--text-white); }
  .battery { width: 62px; height: 28px; border: 3px solid var(--text-white); border-radius: 5px; padding: 3px; position: relative; }
  .battery::after { content: ""; position: absolute; right: -9px; top: 7px; width: 5px; height: 10px; background: var(--text-white); border-radius: 0 2px 2px 0; }
  .battery span { display: block; height: 100%; background: var(--text-white); border-radius: 2px; }

  .nav-bar {
    height: 180px; background: linear-gradient(var(--nav-blue-top), var(--nav-blue-bottom));
    display: flex; align-items: center; justify-content: space-between; padding: 0 40px; flex-shrink: 0;
  }
  .nav-title { font-size: 52px; font-weight: 500; }
  .nav-back, .avatar { width: 120px; }
  .avatar {
    height: 120px; border-radius: 50%; border: 5px solid var(--control-border);
    background: radial-gradient(circle at 50% 40%, #d9b49a, #5b3a2c 75%);
  }

  .toolbar {
    height: 208px; background: var(--toolbar-blue);
    display: flex; align-items: center; gap: 22px; padding: 0 40px; flex-shrink: 0;
  }
  .select-box, .info-button {
    height: 128px; border: 3px solid var(--control-border); border-radius: 14px;
    background: var(--control-blue); display: flex; align-items: center;
  }
  .select-box { flex: 1; padding: 0 36px; font-size: 42px; }
  .select-label { width: 260px; }
  .select-value { flex: 1; text-align: center; }
  .info-button { width: 190px; justify-content: center; }

  .chart-panel {
    height: 1286px; flex-shrink: 0;
    background: linear-gradient(var(--panel-navy), var(--panel-navy-deep));
    position: relative;
  }
  .sleep-chart { position: absolute; left: 0; top: 0; }

  .hero-photo {
    flex: 1; border-top: 10px solid var(--photo-light);
    background: linear-gradient(100deg, var(--photo-warm) 0%, var(--photo-light) 35%, var(--photo-pink) 60%, var(--photo-light) 100%);
  }
</style>
</head>
<body>
<main class="app-screen">
  <header class="status-bar">
    <div class="status-left">
      <span class="signal-dots"><i></i><i></i><i></i><i></i><i class="off"></i></span>
      <span class="carrier">NOVA</span>
      <svg width="36" height="28" viewBox="0 0 36 28" aria-hidden="true">
        <path d="M2 10a23 23 0 0 1 32 0M8 16a14 14 0 0 1 20 0M14 22a6 6 0 0 1 8 0" stroke="#fff" stroke-width="4" fill="none" stroke-linecap="round"/>
      </svg>
    </div>
    <span class="clock">4:21 PM</span>
    <div class="status-right">
      <svg width="20" height="32" viewBox="0 0 20 32" aria-hidden="true">
        <path d="M3 9l13 13-7 7V3l7 7L3 23" stroke="#fff" stroke-width="3" fill="none"/>
      </svg>
      <span>100%</span>
      <span class="battery"><span></span></span>
    </div>
  </header>

  <nav class="nav-bar">
    <svg class="nav-back" width="120" height="60" viewBox="0 0 120 60" aria-label="Back">
      <path d="M34 8L12 30l22 22" stroke="#fff" stroke-width="6" fill="none" stroke-linecap="round" stroke-linejoin="round"/>
    </svg>
    <h1 class="nav-title">Sleep Chart</h1>
    <div class="avatar" role="img" aria-label="User profile photo"></div>
  </nav>

  <section class="toolbar">
    <div class="select-box">
      <span class="select-label">Show :</span>
      <span class="select-value">Sleep Efficiency</span>
      <svg width="36" height="22" viewBox="0 0 36 22" aria-hidden="true"><path d="M2 2h32L18 20z" fill="#fff"/></svg>
    </div>
    <div class="info-button">
      <svg width="72" height="72" viewBox="0 0 72 72" aria-label="Info">
        <circle cx="36" cy="36" r="32" stroke="#fff" stroke-width="5" fill="none"/>
        <circle cx="36" cy="20" r="5" fill="#fff"/>
        <rect x="32" y="30" width="8" height="26" rx="2" fill="#fff"/>
      </svg>
    </div>
  </section>

  <section class="chart-panel">
    <svg class="sleep-chart" width="1200" height="1286" viewBox="0 0 1200 1286" aria-label="Sleep efficiency chart">
      <defs>
        <pattern id="chart-grid" width="22" height="22" patternUnits="userSpaceOnUse">
          <path d="M22 0V22H0" fill="none" stroke="rgba(255,255,255,0.08)" stroke-width="2"/>
        </pattern>
      </defs>
      <text x="60" y="86" fill="#fff" font-family="Roboto, Arial, sans-serif" font-size="40" font-weight="700" letter-spacing="1">SLEEP CHART</text>
      <g transform="translate(1110 68)" stroke="var(--refresh-grey)" stroke-width="5" fill="none" stroke-linecap="round">
        <path d="M-22 -4a22 22 0 0 1 40 -8"/>
        <path d="M22 4a22 22 0 0 1 -40 8"/>
        <path d="M20 -26v14h-14M-20 26v-14h14"/>
      </g>
      <rect x="120" y="204" width="1050" height="1028" fill="url(#chart-grid)"/>
      <path d="M120 697 C200 690 250 600 300 440 C340 330 390 640 463 646 C560 652 640 560 698 554 C760 560 840 680 927 667 C1000 655 1060 600 1090 615 C1120 630 1130 680 1145 697 L1145 1232 L120 1232 Z"
            fill="var(--chart-fill)" fill-opacity="0.85" stroke="var(--chart-line)" stroke-width="4"/>
      <line x1="120" y1="204" x2="120" y2="1232" stroke="var(--axis-line)" stroke-width="3"/>
      <line x1="120" y1="1232" x2="1170" y2="1232" stroke="var(--axis-line)" stroke-width="3"/>
      <g fill="var(--text-soft)" font-family="Roboto, Arial, sans-serif" font-size="26" text-anchor="end">
        <text x="100" y="213">100</text>
        <text x="100" y="470">75</text>
        <text x="100" y="727">50</text>
        <text x="100" y="984">25</text>
        <text x="100" y="1241">0</text>
      </g>
      <rect x="592" y="486" width="212" height="48" rx="4" fill="var(--tag-green)"/>
      <path d="M686 534h24l-12 10z" fill="var(--tag-green)"/>
      <text x="698" y="518" fill="#fff" font-family="Roboto, Arial, sans-serif" font-size="26" text-anchor="middle">5 at 4:07 am</text>
      <circle cx="698" cy="554" r="9" fill="#fff"/>
    </svg>
  </section>

  <div class="hero-photo" role="img" aria-label="Photo of a tired young woman lying awake in bed"></div>
</main>
</body>
</html>
```